Die Zusammenarbeit mit Lora Becker war super. Sie ging sehr engagiert auf meine Wünsche ein und ich habe letztendlich mehr erhalten, als ich eigentlich erwartet habe - PHANTASTISCH !
Zielgruppe
Es geht bei dem Projekt ( Briefpapier ) darum mein Buch zu promoten;:
Rechtsberatung für die Geschäftsführer von Etiketten- und Verpackungsdruckereien
Titel alles auf Papier bringen ( Cover im Anhang )
Darüber hinaus soll eben auch meine geschäftliche Funktion erläutert werden
Aufgabenstellung
Es sollen mindestens alle Elemente des Briefpapierentwurfs ( Anhang ) enthalten sein. Gerne auch weitere Elemente meiner Vita ( Speaker etc. )

```html
<!DOCTYPE html>
<html lang="de">
<head>
<meta charset="utf-8">
<title>Briefbogen Henrik Walden</title>
<link rel="stylesheet" href="https://fonts.googleapis.com/css2?family=Yanone+Kaffeesatz:wght@300;400&family=Arimo:wght@400&display=swap">
<style>
  :root{
    --stage:#444444;
    --paper:#ffffff;
    --ink:#1c1c1c;
    --muted:#8a8a8a;
    --accent:#f7b90f;
    --cover-dark:#232323;
    --cover-mid:#3a3a3a;
    --on-dark:#f2f2f2;
  }
  *{margin:0;padding:0;box-sizing:border-box}
  html,body{width:1200px;height:800px;overflow:hidden;background:var(--stage)}
  .letterhead{
    position:absolute;left:331px;top:20px;width:537px;height:760px;
    background:var(--paper);overflow:hidden;
    font-family:"Yanone Kaffeesatz",sans-serif;font-weight:300;color:var(--ink);
  }
  .return-address{position:absolute;left:51px;top:121px;font-size:7px;white-space:nowrap}
  .return-address .sender{color:var(--muted)}
  .fold-mark{position:absolute;left:13px;height:1px;background:var(--muted)}
  .fold-mark.upper{top:269px;width:13px}
  .fold-mark.lower{top:380px;width:7px}
  .date-line{position:absolute;left:51px;top:263px;font-size:9.5px;white-space:nowrap}
  .reference{position:absolute;left:51px;top:284px;font-size:23px;color:var(--muted);white-space:nowrap}
  .salutation{position:absolute;left:51px;top:334px;font-size:10px}
  .letter-body{position:absolute;left:51px;top:360px;width:321px;font-size:10px;line-height:13px}
  .letter-body p{margin-bottom:13px;text-align:justify}
  .closing{position:absolute;left:51px;top:555px;font-size:10px}
  .signature{position:absolute;left:51px;top:578px;width:166px;height:24px;background:linear-gradient(90deg,#efefef,#fafafa)}
  .signed-name{position:absolute;left:51px;top:611px;font-size:10px}

  .book-cover{position:absolute;left:397px;top:0;width:140px;height:205px;
    background:radial-gradient(ellipse at 70% 55%,var(--cover-mid),var(--cover-dark) 70%)}
  .book-cover .portrait{position:absolute;left:55px;top:36px;width:85px;height:140px;
    background:linear-gradient(180deg,#6b6b6b 0%,#2c2c2c 45%,#1a1a1a 100%);border-radius:40px 40px 0 0;opacity:.7}
  .book-cover .cover-author{position:absolute;top:19px;left:0;width:100%;text-align:center;
    font-family:"Arimo",sans-serif;font-size:4.5px;color:var(--accent)}
  .book-cover .cover-title{position:absolute;left:24px;top:42px;font-family:"Arimo",sans-serif;
    font-size:9.5px;line-height:11px;color:var(--accent)}
  .book-cover .cover-caption{position:absolute;left:8px;bottom:17px;width:124px;text-align:center;
    font-family:"Arimo",sans-serif;font-size:4px;line-height:5px;color:var(--on-dark)}

  .sender-panel{position:absolute;right:77px;text-align:right}
  .sender-name{top:222px;font-size:22px;line-height:20px;color:var(--muted)}
  .sender-roles{top:275px;font-size:8px;line-height:9px}
  .sender-roles p{margin-bottom:4px}
  .sender-contact{top:618px;font-size:8px;line-height:9px}
  .sender-contact p{margin-bottom:4px}

  .claim{position:absolute;left:51px;top:706px;font-family:"Arimo",sans-serif;font-size:23px;line-height:28px;color:var(--accent);white-space:nowrap}
  .claim-band{position:absolute;left:0;bottom:0;width:100%;height:19px;background:var(--accent)}
</style>
</head>
<body>
<main class="letterhead">
  <div class="return-address"><span class="sender">Henrik Walden</span> . Musterstraße 1 . 12345 Musterhausen</div>

  <div class="fold-mark upper"></div>
  <div class="fold-mark lower"></div>

  <div class="date-line">Musterhausen, 31. Dezember 2022</div>
  <div class="reference">Geschäfts-Nr. FE1221205-L/K08</div>

  <div class="salutation">Sehr geehrter Herr Mustermeier,</div>
  <div class="letter-body">
    <p>Lorem ipsum dolor sit amet, consectetuer adipiscing elit. Aenean commodo ligula eget dolor. Aenean massa. Cum sociis natoque penatibus et magnis dis parturient montes, nascetur ridiculus mus. Donec quam felis, ultricies nec, pellentesque eu, pretium quis, sem.</p>
    <p>Nulla consequat massa quis enim. Donec pede justo, fringilla vel, aliquet nec, vulputate eget, arcu. In enim justo, rhoncus ut, imperdiet a, venenatis vitae, justo. Nullam dictum felis eu pede mollis pretium. Integer tincidunt.</p>
    <p>Cras dapibus. Vivamus elementum semper nisi. Aenean vulputate eleifend tellus. Aenean leo ligula, porttitor eu, consequat vitae, eleifend ac, enim. Aliquam lorem ante, dapibus in, viverra quis, feugiat a, tellus. Phasellus viverra<br>nulla ut metus varius laoreet. Quisque rutrum. Aenean imperdiet. Etiam ultricies nisi vel augue. Curabitur ullamcorper ultricies nisi. Nam eget dui.</p>
  </div>

  <div class="closing">Mit freundlichen Grüßen</div>
  <div class="signature" role="img" aria-label="Handschriftliche Unterschrift von Henrik Walden"></div>
  <div class="signed-name">Henrik Walden</div>

  <aside class="book-cover">
    <div class="portrait" role="img" aria-label="Porträtfoto des Autors im dunklen Anzug vor dunklem Hintergrund"></div>
    <div class="cover-author">Henrik Walden</div>
    <div class="cover-title">Alles auf<br>Papier<br>bringen!</div>
    <div class="cover-caption">Verpackungsdruck: Klare Verträge<br>schützen Ihr Geschäft.</div>
  </aside>

  <div class="sender-panel sender-name">Henrik<br>Walden</div>
  <div class="sender-panel sender-roles">
    <p>Geschäftsführender<br>Gesellschafter der<br>Klarvertrag<br>Beratungsgesellschaft<br>mbH</p>
    <p>Gründer der<br>„Initiative Klare Zeichen“</p>
    <p>Buchautor</p>
  </div>
  <div class="sender-panel sender-contact">
    <p>Lindenweg 4</p>
    <p>34117<br>Kassel</p>
    <p>info@klarvertrag.de</p>
    <p>+49 151 4477 309</p>
  </div>

  <div class="claim">Alles auf Papier bringen!</div>
  <div class="claim-band"></div>
</main>
</body>
</html>
```